Tradeshow Booth, Banners & Brochure Design

Corvin Meridian (www.corvinmeridian.example) is a Veltrax Partner specializing in developing products and customizations for Veltrax Ledgerline QP. The purpose of this project is to develop a unified approach to graphic design for our tradeshow booth, banners and product literature. This should result in completed designs for the booth and banners, and several templates that can be used to create our product literature.

***WE WILL ONLY LOOK THROUGH THE FIRST 100 SUBMISSIONS***
Updates

Reason: We have received some requests for an extended deadline, and we would like to encourage more submissions, so we are extending the deadline by two days. Please let us know if you have any questions or need clarification on our design brief.

Thanks for the submissions and questions everyone.  I will get answers to your questions, and more detailed specs, posted within the next couple of hours.  I will also provide detailed feedback to your designs within that time.

Q:  How large should each item be – what is the approximate number of words/lines, columns/rows?

 

-          We have updated the Content Type list to cut it down and simplify this.  For word count, we are attaching the text for our NEW brochure on WMS, which we intend to be a 4 page brochure.  We have labeled each section according to content type.  This can be used as a guide for how much text each content area must be able to accommodate.  You can even pull the raw text straight from the word file for your design.  The CCEM brochure, already included, is an OLD brochure, and represents a design that we are trying to evolve beyond.

 

-          Keep in mind that the 4 page product brochure will be a 17” by 11” single sheet, folded.  The 2 page product brochure will be a single 8.5” by 11” sheet, printed on both sides.

 

-          For the 2 page product brochure, assume something that looks like half of the 4 page design.  For example, we will be creating one brochure for “Financials” which comprises two products.  Product A will go on the front, and Product B on the back.  We will still need to allow for contact information and the other content types as specified.

 

-          For the 4 page corporate overview, we have attached our current corporate overview for reference, and labeled the content types.  Again, feel free to pull raw text directly from this for purposes of your design – though remember, this OLD brochure represents a design we are trying to evolve beyond.

 

-          For images (screenshots, stock photography, diagrams, etc) we are thinking we would like to see about 4 on the 4 page brochure, but only 1-2 for the 2 page brochure.  The corporate overview can have suitable imagery at your discretion.

 

-          We would like to see some of the imagery used in the Tradeshow materials (booth, banners) carried across to the brochures.

 

 

 

Q:  What are the detailed print guidelines, especially in relation to bleeds, etc?

 

-          For all the brochures, use a full bleed.  If your design incorporates a bleed of color across a fold, try to have the bleed going across no more than 25% of the height of the page.  CMYK color, 300DPI, 8.5”w x 11”h.  We will most likely go with 100# paper without too much gloss on it. 

 

-          For all other materials such as booth and banners, no bleeds.  Please see specification sheets for the booth and banners, included below.  Create your designs to the exact size given.

 

 

 

Q:  Will booth graphics be printed as one continuous piece, or will they be applied in sections that are in line with the panel dimensions of the 8 center panels and end caps?

 

-          Graphics are printed as one continuous piece on a large format printer.  They are then cut into the individual panel pieces for shipping and storage.  When the booth is fully assembled, the seams are hardly noticeable unless you are looking for them from a short distance away.

 

-          We are already in possession of one 10’ booth, and will be ordering another, with the associated pieces, to create the 20’ booth.  The booth comprises a support structure, and the actual graphics panels which are attached to the front.  The overall 20’ design should take into account the fact that we will, in the future, attend tradeshows with only a 10’ booth, so only half of the panels will be used.  We would like to be able to mix and match our four categories to suit the show.

Reason: We are extending the deadline one more time to allow Tamsin and anyone else who needs the extra time for the brochure design.

Please prioritize your brochure design at this time.  We are interested in receiving feedback on deadlines - if you can confirm that you will submit a design but need more time to do so, we would like to hear from you.

Reason: To provide time for solid designs from all the designers who have been invited, we are extended the deadline one more time. This will be the final extension.

Target Market(s)

Corporate Clients

Industry/Entity Type

Graphic Design

Requirements
Must have
• TRADESHOW SPECIFIC
1. Graphics for 10'x20' “Heronfold” Tradeshow Booth
a. Layout should approximate the grid we have mocked up in our preliminary layout – see below. There is a fair amount of flexibility so long as the basic grid, contents and dimensions are adhered to.

2. Graphics needed for 3 retractable banner stands
a. Two banner stands will have dimensions of 24” x 88”
b. The third banner stand will have dimensions of 36” x 88” and will be double-sided. The design for this banner should have the option to be scaled down to 33.5” wide, for a possible additional banner stand being considered.
c. Banners should approximate what is shown in the preliminary layout – see below.
d. All banner stands being used are able to fully extend to 92”- however, the height of the booth itself is 88” and we would like all tradeshow specific elements to be the same height.

PRODUCT LITERATURE
1. Graphic Design and Layout needed for brochures:
a. double-sided one page for Products
b. double-sided two page for Products
c. double-sided two page for Overview

2. Pages would be full bleed letter size 8.5” x 11.

3. Samples are included below to get an idea of common grids and layouts for similar publications, as well as one of our current publications for reference.

4. Product literature must include provisions for all of the content types listed in that document, included below. There is some leeway with image placement – a product brochure doesn’t necessarily have to have stock photos, diagrams, AND software screenshots.

5. The designer will need to indicate what specs are required for software screenshots so that we can generate appropriate files for that use.

COMMON ELEMENTS
• Images need to include stock photos of people in business settings, as well as stock photos related to warehousing, barcoding systems, and supply chains. Other images to be used should include schematics, workflow diagrams, and other items that are related to the areas in which the company works. Each heading on the booth, and each page on the brochures, will need one image at minimum. Images and content laid out next to each other should be thematically related whenever possible. We will also create a small number of simple diagrams in house that will need to be redesigned and recreated in the appropriate format and placed in the designs.
• Clean, high-impact design. The Veltrax Tabular Bookkeeping brochure, included below, is a good example of this.
• Our current logo, included below, needs to have the tagline removed. We are also requesting that a different version of the graphic element in the logo be created, in monochrome but with roughly the same geometry.
• Our new tagline is “Integrated Solutions for Ledgerline QP” but it should not be located directly in the logo area as our current tagline is, “Making systems business-ready”.
• Designs should be produced in print-ready PDF files. We will be using Kestrel Layout Pro R4 to open the PDF files, drop in our copy and other content, and finalize the designs. The PDF files will then be sent directly to our booth production and brochure printing companies.

```html
<!DOCTYPE html>
<html lang="en">
<head>
<meta charset="utf-8">
<title>Corvin Meridian – Retractable Banner</title>
<link href="https://fonts.googleapis.com/css2?family=Arimo:wght@400;700&display=swap" rel="stylesheet">
<style>
  :root {
    --page-bg: #ffffff;
    --banner-border: #3a3a3a;
    --sky-top: #f1f2f3;
    --glass-mid: #8f979e;
    --glass-dark: #4b5158;
    --glass-light: #c9ced3;
    --brand-ink: #2a1a1c;
    --headline-ink: #ffffff;
    --panel-fill: rgba(255, 255, 255, 0.72);
    --list-ink: #1d1d1d;
    --mark-fill: #3a3f8f;
  }
  html, body {
    margin: 0;
    padding: 0;
    width: 1200px;
    height: 1200px;
    overflow: hidden;
    background: var(--page-bg);
    font-family: "Arimo", Arial, sans-serif;
  }
  .canvas {
    position: relative;
    width: 1200px;
    height: 1200px;
  }
  .banner {
    position: absolute;
    left: 457px;
    top: 31px;
    width: 314px;
    height: 1154px;
    border: 1px solid var(--banner-border);
    box-sizing: border-box;
    overflow: hidden;
  }
  .banner-photo {
    position: absolute;
    inset: 0;
    background:
      linear-gradient(100deg, rgba(255,255,255,0) 40%, rgba(40,44,50,0.25) 60%, rgba(255,255,255,0) 70%),
      linear-gradient(180deg,
        var(--sky-top) 0%,
        var(--glass-light) 14%,
        var(--glass-mid) 32%,
        var(--glass-dark) 48%,
        var(--glass-mid) 62%,
        var(--glass-light) 74%,
        var(--glass-mid) 88%,
        var(--glass-dark) 100%);
  }
  .brand {
    position: absolute;
    left: 23px;
    top: 195px;
    height: 58px;
    display: flex;
    align-items: center;
    gap: 26px;
  }
  .brand-mark {
    width: 58px;
    height: 58px;
    background: var(--mark-fill);
  }
  .brand-name {
    font-size: 26px;
    font-weight: 400;
    color: var(--brand-ink);
    line-height: 1;
    letter-spacing: -0.3px;
    white-space: nowrap;
  }
  .headline {
    position: absolute;
    left: 0;
    right: 0;
    top: 440px;
    margin: 0;
    text-align: center;
    font-size: 36px;
    font-weight: 700;
    line-height: 44px;
    color: var(--headline-ink);
    text-shadow: 0 1px 3px rgba(0,0,0,0.35);
  }
  .offer-panel {
    position: absolute;
    left: 30px;
    top: 777px;
    width: 267px;
    height: 172px;
    background: var(--panel-fill);
    border-radius: 0 0 12px 0;
  }
  .offer-list {
    list-style: none;
    margin: 0;
    padding: 29px 0 0 24px;
    font-size: 23px;
    line-height: 28px;
    color: var(--list-ink);
    white-space: nowrap;
  }
  .offer-list li::before {
    content: "•";
    margin-right: 5px;
  }
</style>
</head>
<body>
  <div class="canvas">
    <section class="banner">
      <div class="banner-photo" role="img" aria-label="Upward view of mirrored glass office towers reflecting a cloudy sky"></div>

      <div class="brand">
        <div class="brand-mark"></div>
        <span class="brand-name">Corvin Meridian</span>
      </div>

      <h1 class="headline">Integrated<br>Solutions for<br>Ledgerline QP</h1>

      <div class="offer-panel">
        <ul class="offer-list">
          <li>WMS &amp; Distribution</li>
          <li>Workflow</li>
          <li>Customization</li>
          <li>Financials</li>
        </ul>
      </div>
    </section>
  </div>
</body>
</html>
```